" A LUV Consultoria de TI, possui especializaçao em serviços de implantaçao de ERP Vornalis. Soluçoes sao: Consultoria TI, Fabrica de Software, Treinamento e Outsourcing "

```html
<!DOCTYPE html>
<html lang="pt-BR">
<head>
<meta charset="UTF-8">
<title>LUV Consultoria de TI — Cartão de visita</title>
<link rel="stylesheet" href="https://fonts.googleapis.com/css2?family=Montserrat:wght@400;600&display=swap">
<style>
  :root {
    --teal: #1b9aa0;
    --teal-dark: #14848a;
    --teal-faint: #3fb0b5;
    --white: #ffffff;
    --grey: #707274;
    --backdrop: #e9eaeb;
  }
  * { box-sizing: border-box; margin: 0; padding: 0; }
  html, body { width: 1200px; height: 1200px; overflow: hidden; }
  body {
    background: var(--backdrop);
    font-family: "Montserrat", sans-serif;
    display: flex;
    flex-direction: column;
    align-items: center;
    justify-content: center;
    gap: 60px;
  }
  .card {
    position: relative;
    width: 900px;
    height: 515px;
    overflow: hidden;
    box-shadow: 0 6px 18px rgba(0,0,0,0.12);
  }

  /* Front */
  .card-front { background: var(--white); }
  .front-accent { position: absolute; left: 0; bottom: 0; }
  .brand {
    position: absolute;
    top: 50%; left: 50%;
    transform: translate(-50%, -50%);
    display: flex;
    align-items: center;
    gap: 22px;
  }
  .brand-mark { width: 46px; height: 46px; background: var(--teal); }
  .brand-name {
    font-weight: 600;
    font-size: 44px;
    letter-spacing: 6px;
    color: var(--grey);
  }

  /* Back */
  .card-back { background: var(--teal); color: var(--white); }
  .back-watermark {
    position: absolute;
    left: 60px; top: 50%;
    transform: translateY(-50%);
    font-weight: 600;
    font-size: 190px;
    letter-spacing: 8px;
    color: var(--teal-faint);
    opacity: 0.55;
  }
  .contact {
    position: absolute;
    right: 130px;
    top: 58px;
    text-align: right;
  }
  .contact-name { font-size: 34px; font-weight: 400; }
  .contact-role { font-size: 14px; margin-top: 4px; opacity: 0.85; }
  .contact-list { list-style: none; margin-top: 34px; }
  .contact-list li { font-size: 17px; height: 52px; line-height: 52px; }
  .icon-tab {
    position: absolute;
    right: 0; top: 0;
    width: 90px; height: 330px;
    background: var(--white);
    border-bottom-left-radius: 40px;
    display: flex;
    flex-direction: column;
    align-items: center;
    padding-top: 136px;
    gap: 20px;
  }
  .icon-tab svg { width: 32px; height: 32px; }
</style>
</head>
<body>

<section class="card card-front">
  <svg class="front-accent" width="90" height="300" viewBox="0 0 90 300">
    <path d="M0 0 H50 Q90 0 90 40 V300 H0 Z" fill="var(--teal)"/>
  </svg>
  <div class="brand">
    <span class="brand-mark"></span>
    <span class="brand-name">LUV CONSULTORIA</span>
  </div>
</section>

<section class="card card-back">
  <div class="back-watermark" aria-hidden="true">LUV</div>
  <div class="contact">
    <h1 class="contact-name">Seu N. Sobrenome</h1>
    <p class="contact-role">Cargo / Função na empresa</p>
    <ul class="contact-list">
      <li>(11) 5550-0123 / 5550-0124</li>
      <li>contato@luvconsultoria.com.br</li>
      <li>www.luvconsultoria.com.br</li>
      <li>Seu endereço completo</li>
    </ul>
  </div>
  <div class="icon-tab">
    <svg viewBox="0 0 24 24" aria-label="Telefone"><path d="M6.6 10.8a15 15 0 0 0 6.6 6.6l2.2-2.2a1 1 0 0 1 1-.25 11 11 0 0 0 3.6.6 1 1 0 0 1 1 1V20a1 1 0 0 1-1 1A17 17 0 0 1 3 4a1 1 0 0 1 1-1h3.5a1 1 0 0 1 1 1 11 11 0 0 0 .6 3.6 1 1 0 0 1-.25 1z" fill="var(--teal)"/></svg>
    <svg viewBox="0 0 24 24" aria-label="E-mail"><rect x="3" y="6" width="18" height="12" rx="1.5" fill="none" stroke="var(--teal)" stroke-width="2"/><path d="M3 7l9 6 9-6" fill="none" stroke="var(--teal)" stroke-width="2"/></svg>
    <svg viewBox="0 0 24 24" aria-label="Site"><circle cx="12" cy="12" r="9" fill="none" stroke="var(--teal)" stroke-width="2"/><path d="M3 12h18M12 3c3 3 3 15 0 18M12 3c-3 3-3 15 0 18" fill="none" stroke="var(--teal)" stroke-width="1.6"/></svg>
    <svg viewBox="0 0 24 24" aria-label="Endereço"><path d="M12 2a7 7 0 0 0-7 7c0 5 7 13 7 13s7-8 7-13a7 7 0 0 0-7-7z" fill="var(--teal)"/><circle cx="12" cy="9" r="2.5" fill="var(--white)"/></svg>
  </div>
</section>

</body>
</html>
```